Brimovex business card

Based on company logo and website given , to design a business card temple. Slogan "Your furry friends deserves the best"
Color style please refer to our website

```html
<!DOCTYPE html>
<html lang="en">
<head>
<meta charset="utf-8">
<title>Brimovex business card</title>
<link rel="stylesheet" href="https://fonts.googleapis.com/css2?family=Old+Standard+TT&family=Great+Vibes&display=swap">
<style>
  :root {
    --backdrop: #000000;
    --olive-light: #bcb035;
    --olive-mid: #aaa12f;
    --olive-dark: #928a28;
    --olive-deep: #6f6a19;
    --paper: #ffffff;
  }
  * { margin: 0; padding: 0; box-sizing: border-box; }
  html, body { width: 962px; height: 1200px; overflow: hidden; background: var(--backdrop); }
  .sheet { position: relative; width: 962px; height: 1200px; }
  .card { position: absolute; left: 30px; width: 904px; height: 543px; overflow: hidden; background: var(--olive-light); }
  .card--front { top: 40px; }
  .card--back { top: 625px; }
  .card__waves { position: absolute; inset: 0; width: 100%; height: 100%; }
  .brand {
    position: absolute; font-family: "Old Standard TT", serif; font-weight: 400;
    font-size: 100px; line-height: 1; white-space: nowrap; letter-spacing: -1px;
  }
  .card--front .brand { left: 59px; top: 130px; color: var(--olive-light); }
  .card--back .brand { left: 0; width: 856px; text-align: center; top: 200px; color: var(--paper); }
  .holder { position: absolute; left: 506px; color: var(--paper); font-family: "Old Standard TT", serif; line-height: 1; }
  .holder__name { top: 319px; font-size: 37px; }
  .holder__title { top: 365px; font-size: 25px; }
  .contact { position: absolute; list-style: none; color: var(--paper); font-family: "Old Standard TT", serif; font-size: 19px; }
  .contact li { display: flex; align-items: center; height: 34px; }
  .contact svg { width: 20px; height: 20px; margin-right: 16px; flex: none; fill: var(--paper); }
  .contact--left { left: 62px; top: 386px; }
  .contact--right { left: 550px; top: 420px; }
  .pin { position: absolute; left: 509px; top: 431px; width: 31px; height: 44px; fill: var(--paper); }
  .slogan {
    position: absolute; left: 0; width: 904px; text-align: center; top: 312px;
    font-family: "Great Vibes", cursive; font-size: 54px; color: var(--paper); white-space: nowrap;
  }
</style>
</head>
<body>
<main class="sheet">
  <section class="card card--front">
    <svg class="card__waves" viewBox="0 0 1125 675" preserveAspectRatio="none" aria-hidden="true">
      <rect width="1125" height="675" fill="var(--olive-light)"/>
      <path fill="var(--paper)" d="M0 0 H585 C640 150 720 250 805 290 C620 340 450 358 300 362 C200 350 100 338 0 345 Z"/>
      <path fill="var(--olive-dark)" d="M585 0 H1125 V130 C1000 200 900 260 805 290 C720 250 640 150 585 0 Z"/>
      <path fill="var(--olive-deep)" d="M715 222 C900 228 1050 185 1125 130 C1000 200 900 260 805 290 C770 272 740 250 715 222 Z"/>
      <path fill="var(--olive-mid)" d="M300 362 C550 380 720 520 765 675 H0 V345 Z"/>
      <path fill="var(--olive-dark)" d="M0 345 C250 320 560 420 620 675 H0 Z"/>
    </svg>
    <div class="brand">Brimovex</div>
    <div class="holder holder__name">NAME XXXXXXX</div>
    <div class="holder holder__title">TITLE XXXXXXX</div>
    <ul class="contact contact--left">
      <li><svg viewBox="0 0 20 20" aria-hidden="true"><path d="M1 6 C1 2 19 2 19 6 V8 H14 V6 H6 V8 H1 Z M4 9 H16 L18 18 H2 Z"/><circle cx="10" cy="13" r="2.6" fill="var(--olive-dark)"/></svg>XXXXXXXXXX</li>
      <li><svg viewBox="0 0 20 20" aria-hidden="true"><path d="M1 8 L10 2 L19 8 L10 18 Z"/><path d="M1 8 L10 13 L19 8" fill="none" stroke="var(--olive-dark)" stroke-width="1.2"/></svg>XXXXXXXXXXXXXXXXXX</li>
      <li><svg viewBox="0 0 20 20" aria-hidden="true"><circle cx="10" cy="10" r="8.5" fill="none" stroke="var(--paper)" stroke-width="1.6"/><path d="M10 1.5 V18.5 M1.5 10 H18.5 M3 6 H17 M3 14 H17" stroke="var(--paper)" stroke-width="1.3" fill="none"/><ellipse cx="10" cy="10" rx="4" ry="8.5" fill="none" stroke="var(--paper)" stroke-width="1.3"/></svg>XXXXXXXXXXXXXXXXX</li>
    </ul>
    <svg class="pin" viewBox="0 0 31 44" aria-hidden="true"><path d="M15.5 0 C7 0 0 7 0 15.5 C0 26 15.5 44 15.5 44 C15.5 44 31 26 31 15.5 C31 7 24 0 15.5 0 Z M15.5 9 A6.5 6.5 0 1 1 15.49 9 Z" fill-rule="evenodd"/></svg>
    <ul class="contact contact--right">
      <li>XXXXXXXXXXXX</li>
      <li>XXXXXXXXXXXXXXXXXXX</li>
    </ul>
  </section>

  <section class="card card--back">
    <div class="brand">Brimovex</div>
    <p class="slogan">Your furry friends deserves the best</p>
  </section>
</main>
</body>
</html>
```